Lantern over the Harbor ~ A Widening Passage for Writers

My book is called “Lantern over the Harbor.” Its subtitle is “A Widening Passage for Writers.” It is a book about being a poet, writing poetry, and the ways in which poets are connected to both society and the central energy of the Universe. I want the cover design to be abstract and impressionistic. A suggestion of fireworks or a starburst would be a plus. To be consistent with the 3 other books I have published, I want the font for the title, as well as my name (Dorothea Quillbrake) to be Papyrus. The subtitle font can be something more plain and sans serif, like Arial or Franklin Gothic Book, probably in italics. As for color, I definitely want pale gold (angelic). Possible other complimentary colors could be either light or dark shades of gray, turquoise, rose, rust or red. I'm attaching the back cover text and also three pages from inside the book that have line drawings, to give an example of the interior artwork.
Updates

Forgot to mention: My book is a paperback. Its size will be 8.5" high and 5.5" wide. I'm self-publishing it, and it will be printed by Halvern Printworks in Nebraska, USA. It has 104 pages. I think you need the number of pages, in order to make the spine of the book the correct width.

Target Market(s)

My target market is people who write poetry or are interested in how poetry is written.

Industry/Entity Type

Poetry

Font styles to use
Sans Serif
Other font styles liked:
• Papyrus for the front cover. Arial or another sans serif font on the back cover.

Colors

Designer to choose colors to be used in the design.

Requirements
Must have
• My book cover needs to be inspiring and uplifting, as well as abstract and impressionistic, with kind of a "New Age" feel. I don't want anything that looks rigid and scholarly.
Nice to have
• The book talks about the connection poets have to the Universe and the Creative Energy at the center of everything. The cover should convey that Energy.
Should not have
• My cover should not be realistic, logical or straight-laced. I want something that feels free, imaginative and unfettered.

```html
<!DOCTYPE html>
<html lang="en">
<head>
<meta charset="utf-8">
<title>Lantern over the Harbor — Cover Wrap</title>
<link rel="stylesheet" href="https://fonts.googleapis.com/css2?family=Cinzel:wght@400;700&family=Marcellus&family=IBM+Plex+Sans:ital,wght@0,400;0,700;1,400;1,700&family=Arimo:ital@1&display=swap">
<style>
  :root {
    --paper: #ffffff;
    --night: #000000;
    --gold: #f4e93c;
    --line-gold: #b9a66a;
    --ink-light: #ffffff;
    --glow-core: #f2f4ff;
  }
  * { margin: 0; padding: 0; box-sizing: border-box; }
  html, body { width: 1200px; height: 900px; overflow: hidden; background: var(--paper); }
  .cover-wrap { position: relative; width: 1200px; height: 900px; background: var(--paper); }
  .cover-field {
    position: absolute; left: 25px; top: 25px; width: 1150px; height: 850px;
    background: var(--night); overflow: hidden;
  }
  .starburst {
    position: absolute; inset: 0;
    background:
      radial-gradient(circle at 880px 445px, var(--glow-core) 0, rgba(200,210,255,.85) 45px, rgba(110,130,240,.55) 120px, rgba(50,70,200,.35) 230px, rgba(20,30,110,.18) 380px, rgba(0,0,0,0) 560px),
      radial-gradient(ellipse 520px 160px at 880px 445px, rgba(90,110,230,.35), rgba(0,0,0,0) 100%);
  }
  .back-copy {
    position: absolute; left: 59px; top: 47px; width: 430px;
    font-family: "IBM Plex Sans", Arial, sans-serif; font-size: 15px; line-height: 19.5px;
    color: var(--ink-light); text-align: justify;
  }
  .back-copy p { margin-bottom: 19.5px; }
  .back-copy .book-title { font-weight: 700; font-style: italic; letter-spacing: -0.3px; }
  .back-copy .chapters { display: block; text-align: center; }
  .author-photo {
    float: right; width: 90px; height: 126px; margin: 0 0 4px 12px;
    background: linear-gradient(160deg, #9a8670, #c9b9a8 45%, #6f8f7e);
  }
  .barcode-space {
    position: absolute; left: 149px; top: 641px; width: 235px; height: 139px; background: var(--paper);
  }
  .spine-title, .spine-author {
    position: absolute; writing-mode: vertical-rl; color: var(--gold);
    font-family: "Cinzel", serif;
  }
  .spine-title { left: 562px; top: 48px; font-size: 22px; letter-spacing: 6.6px; }
  .spine-author { left: 566px; top: 578px; font-size: 14px; letter-spacing: 2.4px; }
  .front-title {
    position: absolute; left: 655px; top: 40px; width: 450px; text-align: center;
    font-family: "Cinzel", serif; line-height: 1;
  }
  .front-title .main { display: block; color: var(--gold); font-size: 84px; font-weight: 700; letter-spacing: 1px; }
  .front-title .link { display: block; color: var(--ink-light); font-size: 40px; margin-top: 12px; }
  .front-title .tail { display: block; color: var(--ink-light); font-size: 62px; margin-top: 8px; }
  .subtitle {
    position: absolute; left: 730px; top: 422px; width: 300px; text-align: center;
    font-family: "Arimo", Arial, sans-serif; font-style: italic; font-size: 24px;
    line-height: 30px; letter-spacing: 4px; color: var(--night);
  }
  .byline-rule { position: absolute; left: 0; top: 810px; width: 1150px; height: 1px; background: var(--line-gold); }
  .byline {
    position: absolute; left: 720px; top: 786px; padding: 0 6px; background: var(--night);
    font-family: "Marcellus", serif; font-size: 33px; color: var(--ink-light); line-height: 46px;
  }
</style>
</head>
<body>
<div class="cover-wrap">
  <div class="cover-field">
    <div class="starburst" role="img" aria-label="Abstract blue and white starburst of radiating light rays forming soft wing shapes"></div>

    <section class="back-cover">
      <div class="back-copy">
        <div class="author-photo" role="img" aria-label="Author portrait photograph"></div>
        <p><span class="book-title">Lantern over the Harbor</span> is indeed “A Widening Passage for Writers.” It is written by Dorothea Quillbrake, an exciting, imaginative voice in American poetry.</p>
        <p>In <span class="book-title">Lantern over the Harbor,</span> Dorothea discusses the essential elements of poetry and the process of writing it. She offers an inspiring view of the mission of poets and their connection to both society and the larger forces in the Universe. Her book is motivational, refreshing and irrepressibly optimistic.</p>
        <p>The seven intriguing chapters in <em>Lantern over the Harbor are</em>
          <span class="chapters">LIBERATION ~ EXPERIENCE ~ WORDS ~ POETRY ~<br>INTEGRITY ~ BEAUTY ~ CREATION</span></p>
        <p>For over 50 years, Dorothea has been a teacher of writing and poetry. Since 2007, she has published three books of her poems: <em>Mind the Rain Barrel, The Pale Hem of Forever</em> and <em>The Wide Velvet Hush.</em> Her work overflows with her characteristically rich images and quirky metaphors. It runs the gamut from subtle eroticism to abject grief, from defiant rage to philosophical meditation, and from borderline blasphemy to lyrical fantasy.</p>
        <p>Dorothea has been called by critic Conrad Ellsby “a poet to be reckoned with; bright, feisty, compassionate.” (<em>The Valley Courier,</em> Millbrook, PA). Author Lorna Vantrees (<em>“Thornfield Lane,”</em> 2011) says Dorothea’s poetry is like “a perpetual Surprise Party ~ memorable, insightful and thematically fascinating.”</p>
      </div>
      <div class="barcode-space"></div>
    </section>

    <section class="spine">
      <div class="spine-title">LANTERN OVER THE HARBOR</div>
      <div class="spine-author">DOROTHEA QUILLBRAKE</div>
    </section>

    <section class="front-cover">
      <h1 class="front-title">
        <span class="main">LANTERN</span>
        <span class="link">OVER THE</span>
        <span class="tail">HARBOR</span>
      </h1>
      <p class="subtitle">A<br>Widening<br>Passage<br>for Writers</p>
      <div class="byline-rule"></div>
      <div class="byline">Dorothea Quillbrake</div>
    </section>
  </div>
</div>
</body>
</html>
```